Bluewake Skipper Services LLC

I'd like business cards with a logo and words to describe my services and qualifications. I want to emphasize the wide variety of services offered and my professional qualifications. Words to include "Bluewake Skipper Services LLC", "Motor and Sailing Vessel Delivery, Charter, Surveys, Towing and Instruction". Qualifications I would like to include are "Captain Rob Dellaway, NMLB Master Mariner, 200 ton, Ocean". Include address, phone and email: "48215 Hollowmere Lane, Kestrel Point, NC 28417, (C) 555-492-6078, BluewakeSkipperServices@postvelo.net"

Target Market(s)

I am targeting recreational boaters and commercial customers that need people to operate their boats for charter or delivery to another location.

Industry/Entity Type

boat selling/buying, boat charter, boat recreation

Logo Text

"Motor and Sailing Vessel Delivery, Charters, Surveys, Towing and Instruction"

Requirements
Must have
• A professional and nautical look.
Nice to have
• May be nice to have a muted chart as the background design
Should not have
• colors or design that obscure the message of offering a wide range of professional boat captain services

```html
<!DOCTYPE html>
<html lang="en">
<head>
<meta charset="utf-8">
<title>Bluewake Skipper Services LLC — Business Cards</title>
<link href="https://fonts.googleapis.com/css2?family=Noto+Serif:ital,wght@0,400;0,700;1,700&display=swap" rel="stylesheet">
<style>
  :root {
    --stage: #4f5f52;
    --ink: #2b2622;
    --paper-mint: #e3efe2;
    --paper-cream: #ede3cf;
    --paper-sand: #d8c29a;
    --paper-tan: #c6a774;
    --paper-sage: #c9d7b3;
    --map-blue: #4f9ac4;
    --map-teal: #2ea4b8;
    --map-red: #b4553e;
    --map-clay: #b9713f;
  }
  * { box-sizing: border-box; margin: 0; padding: 0; }
  html, body { width: 1200px; height: 1200px; overflow: hidden; }
  body {
    background: var(--stage);
    font-family: "Noto Serif", Georgia, serif;
    color: var(--ink);
    display: flex;
    flex-direction: column;
    align-items: center;
    justify-content: center;
    gap: 60px;
  }
  .card {
    position: relative;
    width: 840px;
    height: 480px;
    overflow: hidden;
    background:
      radial-gradient(ellipse at 20% 10%, var(--paper-mint) 0%, transparent 55%),
      radial-gradient(ellipse at 85% 90%, var(--paper-tan) 0%, transparent 60%),
      radial-gradient(ellipse at 10% 95%, var(--paper-sage) 0%, transparent 50%),
      linear-gradient(135deg, var(--paper-mint) 0%, var(--paper-cream) 45%, var(--paper-sand) 100%);
  }

  /* Front */
  .chart-area {
    position: absolute;
    left: 0;
    top: 70px;
    width: 320px;
    height: 410px;
    border-radius: 0 60% 40% 0 / 0 40% 60% 0;
    background: linear-gradient(180deg, var(--map-blue) 0%, var(--map-teal) 45%, var(--map-red) 70%, var(--map-clay) 100%);
    opacity: 0.85;
  }
  .qualifications {
    position: absolute;
    right: 40px;
    top: 34px;
    text-align: right;
    font-size: 19px;
    line-height: 1.25;
  }
  .qualifications .captain-name { font-size: 27px; font-weight: 700; font-style: italic; }
  .services {
    position: absolute;
    left: 340px;
    top: 180px;
    width: 460px;
    text-align: center;
    font-weight: 700;
    font-size: 23px;
    line-height: 1.3;
  }
  .contact-front {
    position: absolute;
    right: 40px;
    bottom: 34px;
    text-align: right;
    font-size: 19px;
    line-height: 1.35;
  }

  /* Back */
  .brand {
    position: absolute;
    top: 50px;
    left: 0;
    right: 0;
    display: flex;
    flex-direction: column;
    align-items: center;
    gap: 18px;
  }
  .brand-circle {
    width: 150px;
    height: 150px;
    border: 5px solid var(--ink);
    border-radius: 50%;
  }
  .brand-name { font-size: 30px; font-weight: 700; }
  .contact-back {
    position: absolute;
    left: 0;
    right: 0;
    bottom: 60px;
    text-align: center;
    font-weight: 700;
    font-size: 20px;
    line-height: 1.4;
  }
</style>
</head>
<body>
  <section class="card card-front">
    <div class="chart-area" role="img" aria-label="Watercolour map of North and South America"></div>
    <div class="qualifications">
      <p class="captain-name">Captain Rob Dellaway</p>
      <p>NMLB Master Mariner</p>
      <p>200 ton, Ocean</p>
    </div>
    <p class="services">Motor and Sailing Vessel Delivery,<br>Charter, Surveys,<br>Towing and Instruction</p>
    <div class="contact-front">
      <p>48215 Hollowmere Lane,</p>
      <p>Kestrel Point, NC 28417,</p>
      <p>© 555-492-6078,</p>
      <p>BluewakeSkipperServices@postvelo.net</p>
    </div>
  </section>

  <section class="card card-back">
    <div class="brand">
      <div class="brand-circle"></div>
      <p class="brand-name">Bluewake Skipper Services LLC</p>
    </div>
    <div class="contact-back">
      <p>48215 Hollowmere Lane, Kestrel Point, NC 28417,</p>
      <p>© 555-492-6078,</p>
      <p>BluewakeSkipperServices@postvelo.net</p>
    </div>
  </section>
</body>
</html>
```